Tom Verlane

I am the director of Casa Del Humo International. We make premium cigars

I want an insanely beautiful card that directly attracts attention. Do your best. The card can use emboss, foil, laser-cut metal or anything else. Make it stand out, but also elegant.

Target Market(s)

Cigar Distributors

Industry/Entity Type

Cigars

Contact Information for Business Card

Email: tom.verlane@verlanos.com + Logos (attached) + Position: Director + 'High-End Cigars'

Colors

Designer to choose colors to be used in the design.

Requirements
Nice to have
• Please check us out at www.casadelhumo.com and try to use our colors and styles

```html
<!DOCTYPE html>
<html lang="en">
<head>
<meta charset="utf-8">
<title>Casa Del Humo International – Business Card</title>
<link rel="stylesheet" href="https://fonts.googleapis.com/css2?family=Crimson+Text:wght@400;600&family=Tinos:wght@400;700&family=Arimo:wght@400&display=swap">
<style>
  :root {
    --backdrop: #1b1b1b;
    --card: #0f0f0f;
    --ink: #f4f2ef;
    --accent: #c8142c;
    --rule: #9a2a2e;
    --emboss: #7d7d7d;
  }
  html, body {
    margin: 0;
    width: 1200px;
    height: 1059px;
    overflow: hidden;
    background: var(--backdrop);
  }
  .card {
    position: absolute;
    left: 172px;
    top: 286px;
    width: 855px;
    height: 487px;
    border-radius: 30px;
    background: var(--card);
    color: var(--ink);
  }
  .company {
    position: absolute;
    top: 24px;
    left: 0;
    width: 100%;
    margin: 0;
    text-align: center;
    font: 400 42px/1 "Crimson Text", serif;
    letter-spacing: 0.5px;
  }
  .divider {
    position: absolute;
    left: 79px;
    top: 86px;
    width: 697px;
    height: 20px;
  }
  .location {
    position: absolute;
    top: 126px;
    width: 100%;
    text-align: center;
    font: 400 28px/1 "Arimo", sans-serif;
  }
  .person-name {
    position: absolute;
    top: 188px;
    width: 100%;
    text-align: center;
    font: 700 38px/1 "Tinos", serif;
    color: var(--accent);
  }
  .person-role {
    position: absolute;
    top: 236px;
    width: 100%;
    text-align: center;
    font: 400 22px/1 "Tinos", serif;
  }
  .contact-rule {
    position: absolute;
    left: 39px;
    top: 277px;
    width: 777px;
    height: 2px;
    background: var(--accent);
  }
  .contact {
    position: absolute;
    top: 295px;
    height: 26px;
    display: flex;
    align-items: center;
    gap: 12px;
    font: 400 22px/1 "Tinos", serif;
  }
  .contact svg { width: 24px; height: 24px; flex: none; }
  .contact-phone { left: 39px; }
  .contact-email { left: 243px; gap: 18px; }
  .contact-web { left: 540px; gap: 16px; }
  .lines {
    position: absolute;
    top: 365px;
    left: 0;
    width: 100%;
    height: 70px;
  }
  .line-name {
    position: absolute;
    top: 22px;
    transform: translateX(-50%);
    white-space: nowrap;
    font: 400 26px/1 "Crimson Text", serif;
    color: var(--emboss);
  }
  .line-vega { left: 240px; }
  .line-brasa { left: 425px; }
  .line-cumbre { left: 605px; }
</style>
</head>
<body>
  <div class="card">
    <h1 class="company">CASA DEL HUMO INTERNATIONAL</h1>

    <svg class="divider" viewBox="0 0 697 20" aria-hidden="true">
      <line x1="0" y1="10" x2="697" y2="10" stroke="var(--rule)" stroke-width="1.2"/>
      <rect x="342" y="3" width="13" height="13" fill="var(--accent)" transform="rotate(45 348.5 9.5)"/>
    </svg>

    <div class="location">VALLE SERENO - HONDURAS</div>

    <div class="person-name">Tom Verlane</div>
    <div class="person-role">Managing Director</div>

    <div class="contact-rule"></div>

    <div class="contact contact-phone">
      <svg viewBox="0 0 24 24" aria-hidden="true">
        <path fill="var(--accent)" d="M6.6 10.8a15.2 15.2 0 0 0 6.6 6.6l2.2-2.2a1 1 0 0 1 1-.25 11.4 11.4 0 0 0 3.6.57 1 1 0 0 1 1 1V20a1 1 0 0 1-1 1A17 17 0 0 1 3 4a1 1 0 0 1 1-1h3.5a1 1 0 0 1 1 1c0 1.25.2 2.45.57 3.57a1 1 0 0 1-.25 1z"/>
        <path fill="none" stroke="var(--accent)" stroke-width="1.6" d="M14 3.5a7 7 0 0 1 6.5 6.5M14 7a3.5 3.5 0 0 1 3 3"/>
      </svg>
      <span>123 456 7890</span>
    </div>

    <div class="contact contact-email">
      <svg viewBox="0 0 24 24" aria-hidden="true">
        <path fill="var(--accent)" d="M1 5h22v14H1z"/>
        <path fill="none" stroke="var(--card)" stroke-width="1.6" d="M1.5 5.5 12 13l10.5-7.5"/>
      </svg>
      <span>tom.verlane@verlanos.com</span>
    </div>

    <div class="contact contact-web">
      <svg viewBox="0 0 24 24" aria-hidden="true">
        <circle cx="12" cy="12" r="10.5" fill="var(--accent)"/>
        <path fill="var(--card)" d="M7 5.5c2 .5 3 2 2.5 3.5S7 10 7.5 12s2.5 2 2.5 4-1 3-1 4.5A9 9 0 0 1 4 9c1-.5 1.8-2.5 3-3.5zM15 4.5c1 1.5 0 3 1.5 3.5s3 .5 4 2.5a9 9 0 0 1-1 6.5c-1-1-1.5-2.5-3-2.5s-2-1.5-1.5-3S13.5 9 13 7.5s1-2.5 2-3z"/>
      </svg>
      <span>www.casadelhumo.com</span>
    </div>

    <div class="lines">
      <span class="line-name line-vega">Vega Alta</span>
      <span class="line-name line-brasa">Brasa Lenta</span>
      <span class="line-name line-cumbre">Cumbre Real</span>
    </div>
  </div>
</body>
</html>
```